Commercial & Industrial Electrical - Millwright Maintenance Flyer

Want to create a flyer with picture of Service Man and some of pictures and highlights on the attachment I have attached. We like to use colors of Orange-Blue -Black where possible

```html
<!DOCTYPE html>
<html lang="en">
<head>
<meta charset="utf-8">
<title>Millwright Maintenance Services Flyer</title>
<link href="https://fonts.googleapis.com/css2?family=Inter+Tight:wght@400;500;600;700;800&family=Oswald:wght@600;700&display=swap" rel="stylesheet">
<style>
  :root {
    --ink: #111111;
    --blue: #1c5cf0;
    --orange: #fc6420;
    --yellow: #f5b324;
    --paper: #f4f4f4;
    --paper-light: #fbfbfb;
    --grey-pill: #e4e4e4;
    --steel: #b9bcc0;
  }
  * { margin: 0; padding: 0; box-sizing: border-box; }
  html, body { width: 921px; height: 1200px; overflow: hidden; background: #ffffff; }
  .flyer {
    position: relative; width: 921px; height: 1200px; overflow: hidden;
    background: linear-gradient(120deg, var(--paper-light) 0%, var(--paper) 35%, var(--paper-light) 55%, var(--paper) 100%);
    font-family: "Inter Tight", Arial, sans-serif; color: var(--ink);
  }
  .abs { position: absolute; }

  .title { left: 55px; top: 44px; font-weight: 700; line-height: 1.02; letter-spacing: -1.6px; }
  .title .line-1 { font-size: 45px; display: block; }
  .title .line-2 { font-size: 44px; display: block; letter-spacing: -2px; }

  .banner { background: var(--blue); color: #fff; font-weight: 700; letter-spacing: -1.8px; font-size: 39px; line-height: 1; transform: rotate(-2.2deg); transform-origin: left top; }
  .banner-1 { left: 55px; top: 162px; width: 418px; height: 56px; padding: 10px 0 0 14px; }
  .banner-2 { left: 60px; top: 224px; width: 459px; height: 64px; padding: 12px 0 0 14px; }

  .brand { left: 600px; top: 176px; width: 290px; text-align: center; font-size: 17px; font-weight: 500; line-height: 1.4; color: #2a2a2a; }
  .brand-dot { left: 735px; top: 90px; width: 30px; height: 30px; border-radius: 50%; background: #2a2a2a; }

  .band-left { left: 0; top: 437px; width: 110px; height: 110px; background: var(--orange); }
  .band-right { left: 296px; top: 437px; width: 110px; height: 110px; background: var(--orange); border-radius: 0 55px 55px 0; }
  .machine { left: 58px; top: 312px; width: 290px; height: 268px; background: linear-gradient(160deg, #e6e8ea 0%, var(--steel) 55%, #8e9398 100%); border-radius: 6px; }

  h2 { font-size: 20.5px; font-weight: 700; letter-spacing: -0.8px; line-height: 27px; }
  .body-text { font-size: 15.5px; line-height: 20.6px; letter-spacing: -0.6px; color: #1a1a1a; }

  .millwright-heading { left: 449px; top: 302px; }
  .millwright-body { left: 449px; top: 361px; width: 420px; }

  .pill { left: 512px; top: 692px; width: 420px; height: 110px; border-radius: 55px 0 0 55px; background: var(--grey-pill); }
  .plant { left: 597px; top: 560px; width: 190px; height: 242px; background: linear-gradient(180deg, #cfd3d7 0%, #9aa0a6 60%, #5d6368 100%); border-radius: 4px; }

  .electrical-heading { left: 55px; top: 591px; }
  .electrical-body { left: 55px; top: 653px; width: 455px; }

  .rule { left: 55px; top: 843px; width: 297px; height: 2px; background: linear-gradient(90deg, var(--orange) 0 25%, var(--yellow) 25% 44%, var(--orange) 44% 100%); }

  .industries-heading { left: 54px; top: 861px; font-size: 21px; font-weight: 700; letter-spacing: -1px; line-height: 25px; }
  .industries-heading .accent { color: var(--blue); }
  .industry-list { left: 54px; top: 921px; list-style: none; font-size: 15.5px; letter-spacing: -0.55px; }
  .industry-list li { height: 22.8px; display: flex; align-items: center; gap: 9px; }
  .industry-list svg { width: 9px; height: 10px; flex: none; }

  .worker { left: 336px; top: 914px; width: 128px; height: 238px; border-radius: 60px 60px 10px 10px; background: linear-gradient(180deg, #f1f1f1 0%, #f49a5e 35%, #3d55b8 75%, #8a5a3a 100%); opacity: 0.85; }

  .contact-label { left: 476px; top: 1100px; font-size: 30px; font-weight: 700; letter-spacing: -1px; line-height: 34px; transform: rotate(-90deg); transform-origin: left top; white-space: nowrap; }
  .contact-line { left: 492px; top: 1112px; width: 2px; height: 38px; background: var(--blue); }

  .badge { left: 478px; top: 818px; width: 215px; height: 100px; }
  .badge-24 { position: absolute; left: 0; top: 0; font-family: "Oswald", Arial, sans-serif; font-weight: 700; font-style: italic; font-size: 80px; line-height: 1; color: var(--orange); letter-spacing: -4px; }
  .badge-hour { position: absolute; left: 86px; top: 4px; background: var(--orange); color: #fff; font-family: "Oswald", Arial, sans-serif; font-weight: 700; font-size: 21px; padding: 1px 14px 1px 8px; transform: rotate(-6deg); line-height: 1.1; }
  .badge-words { position: absolute; left: 90px; top: 38px; font-family: "Oswald", Arial, sans-serif; font-weight: 700; line-height: 1; transform: rotate(-6deg); }
  .badge-words .em { display: block; font-size: 17px; color: var(--ink); }
  .badge-words .sv { display: block; font-size: 24px; color: var(--orange); }

  .call { left: 712px; top: 856px; font-size: 16px; font-weight: 700; letter-spacing: -0.7px; line-height: 26px; }
  .call .number { color: var(--orange); }

  .contacts { left: 524px; top: 940px; font-size: 15px; letter-spacing: -0.45px; }
  .contact-row { display: flex; gap: 13px; align-items: flex-start; height: 21px; line-height: 18px; }
  .contact-row svg { width: 12px; height: 12px; margin-top: 3px; flex: none; }
  .contact-row.address { height: 40px; }
  .person { font-weight: 700; font-size: 15px; letter-spacing: -0.6px; line-height: 18px; margin: 3px 0 5px; }
</style>
</head>
<body>
<main class="flyer">

  <h1 class="abs title"><span class="line-1">MILLWRIGHT</span><span class="line-2">Maintenance Services</span></h1>
  <div class="abs banner banner-1">With over 100 years</div>
  <div class="abs banner banner-2">of experience on staff.</div>

  <div class="abs brand-dot"></div>
  <div class="abs brand">Summit Ridge Millwrights &amp;<br>Maintenance</div>

  <div class="abs band-left"></div>
  <div class="abs band-right"></div>
  <div class="abs machine" role="img" aria-label="Photo of a stainless steel industrial processing machine"></div>

  <h2 class="abs millwright-heading">Millwright &amp; Maintenance Services<br>Locally or Nationwide&nbsp; 24/7</h2>
  <p class="abs body-text millwright-body">We provide Millwright/Maintenance and Industrial Rigging services. Our team is skilled in installing, maintaining, repairing, and troubleshooting industrial equipment. We handle turnkey projects as well as emergency repairs to ensure the efficient operation of factories or plants. For Project, Plant, or Equipment, Building Maintenance, we offer comprehensive support. Additionally, we have a fabrication and welding shop for custom build of conveyors, equipment parts, and more.</p>

  <div class="abs pill"></div>
  <div class="abs plant" role="img" aria-label="Photo of an industrial plant building with a tall steel stack and tower"></div>

  <h2 class="abs electrical-heading">Electrical &amp; Maintenance Services<br>Locally or Nationwide 24/7</h2>
  <p class="abs body-text electrical-body">SRMM Electrical Division provides electrical services for commercial and industrial clients. Certified and Licensed electricians manage tasks such as automation/PLC control systems, wiring and repairs, security, cameras, and communications cabling, including VOIP systems, data lines, and thermal imaging for annual inspections. The team is trained and experienced to complete electrical jobs safely and efficiently.</p>

  <div class="abs rule"></div>
  <h3 class="abs industries-heading"><span class="accent">Industries</span> We Have<br>Experience Servicing</h3>
  <ul class="abs industry-list">
    <li><svg viewBox="0 0 9 10"><path d="M2 1l5 4-5 4" fill="none" stroke="#1c5cf0" stroke-width="1.6"/></svg>Food &amp; Beverage</li>
    <li><svg viewBox="0 0 9 10"><path d="M2 1l5 4-5 4" fill="none" stroke="#1c5cf0" stroke-width="1.6"/></svg>Pet Foods</li>
    <li><svg viewBox="0 0 9 10"><path d="M2 1l5 4-5 4" fill="none" stroke="#1c5cf0" stroke-width="1.6"/></svg>Agriculture-Grain &amp; Flour Mills</li>
    <li><svg viewBox="0 0 9 10"><path d="M2 1l5 4-5 4" fill="none" stroke="#1c5cf0" stroke-width="1.6"/></svg>Steel Mills &amp; processing Plants</li>
    <li><svg viewBox="0 0 9 10"><path d="M2 1l5 4-5 4" fill="none" stroke="#1c5cf0" stroke-width="1.6"/></svg>Warehouse &amp; Distribution</li>
    <li><svg viewBox="0 0 9 10"><path d="M2 1l5 4-5 4" fill="none" stroke="#1c5cf0" stroke-width="1.6"/></svg>Water &amp; Wastewater</li>
    <li><svg viewBox="0 0 9 10"><path d="M2 1l5 4-5 4" fill="none" stroke="#1c5cf0" stroke-width="1.6"/></svg>Laundry Plants</li>
    <li><svg viewBox="0 0 9 10"><path d="M2 1l5 4-5 4" fill="none" stroke="#1c5cf0" stroke-width="1.6"/></svg>Textile Plants</li>
    <li><svg viewBox="0 0 9 10"><path d="M2 1l5 4-5 4" fill="none" stroke="#1c5cf0" stroke-width="1.6"/></svg>Data Centers</li>
    <li><svg viewBox="0 0 9 10"><path d="M2 1l5 4-5 4" fill="none" stroke="#1c5cf0" stroke-width="1.6"/></svg>Oil Field &amp; Processing Plants</li>
  </ul>

  <div class="abs worker" role="img" aria-label="3D illustration of a service technician in hard hat and overalls leaning on a large wrench"></div>

  <div class="abs contact-label">Contact Us</div>
  <div class="abs contact-line"></div>

  <div class="abs badge">
    <span class="badge-24">24</span>
    <span class="badge-hour">HOUR</span>
    <span class="badge-words"><span class="em">EMERGENCY</span><span class="sv">SERVICE</span></span>
  </div>

  <p class="abs call">Call <span class="number">720-555-0142</span><br>Leave message</p>

  <div class="abs contacts">
    <div class="contact-row"><svg viewBox="0 0 12 12"><path d="M3 1l2 2.5-1.2 1.3a7 7 0 0 0 3.4 3.4L8.5 7 11 9l-1.2 2C5 11 1 7 1 2.2z" fill="#1c5cf0"/></svg>303-555-0187</div>
    <div class="contact-row address"><svg viewBox="0 0 12 12"><path d="M6 0.5a4 4 0 0 1 4 4c0 3-4 7-4 7s-4-4-4-7a4 4 0 0 1 4-4z" fill="#fc6420"/><circle cx="6" cy="4.5" r="1.5" fill="#fff"/></svg><span>1850 E. Foundry Avenue<br>Unit C400, Denver CO,80216</span></div>
    <div class="person">Mark Holloway</div>
    <div class="contact-row"><svg viewBox="0 0 12 12"><path d="M3 1l2 2.5-1.2 1.3a7 7 0 0 0 3.4 3.4L8.5 7 11 9l-1.2 2C5 11 1 7 1 2.2z" fill="#1c5cf0"/></svg>720-555-0163</div>
    <div class="contact-row"><svg viewBox="0 0 12 12"><rect x="0.5" y="2" width="11" height="8" fill="#1c5cf0"/><path d="M0.5 2.5L6 6.5l5.5-4" fill="none" stroke="#fff" stroke-width="1"/></svg>m.holloway@summitridgemw.com</div>
    <div class="person">Dana Holloway</div>
    <div class="contact-row"><svg viewBox="0 0 12 12"><path d="M3 1l2 2.5-1.2 1.3a7 7 0 0 0 3.4 3.4L8.5 7 11 9l-1.2 2C5 11 1 7 1 2.2z" fill="#fc6420"/></svg>303-555-0129</div>
    <div class="contact-row"><svg viewBox="0 0 12 12"><rect x="0.5" y="2" width="11" height="8" fill="#fc6420"/><path d="M0.5 2.5L6 6.5l5.5-4" fill="none" stroke="#fff" stroke-width="1"/></svg>d.holloway@summitridgemw.com</div>
  </div>

</main>
</body>
</html>
```